Urine collection cup with and without sterile seal sticker

Hello. We need a urine cup label designed please with

Name:
Date of Birth:
Date:
Time:
Temp℃:
Specimen ID:

Product code: KTX-58
Volume markings (e.g., 30 mL, 60 mL, 90 mL).
Vesk Lab Checks logo

Could you please provide one version with the additional sterile sticker extending to the top, and one version without the additional sterile sticker?

```html
<!DOCTYPE html>
<html lang="en">
<head>
<meta charset="utf-8">
<title>Vesk Lab Checks – Urine Cup Labels</title>
<link rel="stylesheet" href="https://fonts.googleapis.com/css2?family=Barlow:wght@500;600;800&display=swap">
<style>
  :root {
    --page-bg: #d7dbe0;
    --label-bg: #ffffff;
    --navy: #1a3d6b;
    --sky: #2a9fe0;
    --white: #ffffff;
  }
  * { box-sizing: border-box; margin: 0; padding: 0; }
  html, body { width: 924px; height: 1200px; overflow: hidden; }
  body {
    background: var(--page-bg);
    font-family: "Barlow", Arial, sans-serif;
    position: relative;
  }
  .cup-label {
    position: absolute;
    left: 139px;
    width: 649px;
    height: 337px;
    background: var(--label-bg);
    box-shadow: -4px 6px 10px rgba(40, 50, 70, 0.35);
  }
  .cup-label--sterile { top: 324px; }
  .cup-label--plain { top: 750px; }

  .record-table {
    position: absolute;
    left: 22px;
    top: 31px;
    width: 496px;
    height: 274px;
    border: 1.5px solid var(--navy);
    border-left: 10px solid var(--navy);
    display: grid;
    grid-template-rows: repeat(5, 1fr);
  }
  .record-row {
    display: flex;
    border-bottom: 1.5px solid var(--navy);
  }
  .record-row:last-child { border-bottom: none; }
  .record-cell {
    flex: 1;
    padding: 6px 0 0 6px;
    color: var(--navy);
    font-size: 18px;
    font-weight: 500;
    letter-spacing: 0.4px;
  }
  .record-cell--half { flex: 0 0 237px; border-right: 9px solid var(--navy); }

  .brand-strip {
    position: absolute;
    left: 541px;
    top: 0;
    width: 108px;
    height: 100%;
    background: var(--navy);
    color: var(--white);
  }
  .sterile-seal {
    position: absolute;
    left: 680px;
    top: 101px;
    width: 108px;
    height: 224px;
    background: var(--navy);
    border-radius: 39px 39px 0 0;
  }
  .sterile-word {
    position: absolute;
    left: 50%;
    top: 33px;
    transform: translateX(-50%);
    writing-mode: vertical-rl;
    font-weight: 800;
    font-size: 42px;
    letter-spacing: 1px;
    color: var(--white);
    line-height: 1;
  }
  .strip-rule {
    position: absolute;
    left: 11px;
    width: 86px;
    height: 2px;
    background: var(--white);
  }
  .brand-mark {
    position: absolute;
    left: 50%;
    top: 26px;
    transform: translateX(-50%);
    display: flex;
    flex-direction: column;
    align-items: center;
    gap: 8px;
  }
  .brand-dot {
    width: 42px;
    height: 42px;
    border-radius: 50%;
    background: var(--sky);
  }
  .brand-name {
    writing-mode: vertical-rl;
    font-weight: 800;
    font-size: 24px;
    line-height: 1;
    color: var(--white);
    white-space: nowrap;
  }
  .volume {
    position: absolute;
    left: 0;
    top: 307px;
    width: 100%;
    text-align: center;
    font-size: 17px;
    font-weight: 500;
    color: var(--white);
  }
</style>
</head>
<body>

  <div class="sterile-seal">
    <span class="sterile-word">STERILE</span>
  </div>

  <section class="cup-label cup-label--sterile">
    <div class="record-table">
      <div class="record-row"><div class="record-cell">NAME</div></div>
      <div class="record-row"><div class="record-cell">DOB</div></div>
      <div class="record-row">
        <div class="record-cell record-cell--half">DATE</div>
        <div class="record-cell">TIME</div>
      </div>
      <div class="record-row"><div class="record-cell">TEMP °C</div></div>
      <div class="record-row"><div class="record-cell">SPECIMEN ID</div></div>
    </div>
    <div class="brand-strip">
      <div class="strip-rule" style="top:-1px"></div>
      <div class="brand-mark">
        <span class="brand-dot"></span>
        <span class="brand-name">Vesk Lab Checks</span>
      </div>
      <div class="strip-rule" style="top:294px"></div>
      <div class="volume">90ml</div>
    </div>
  </section>

  <section class="cup-label cup-label--plain">
    <div class="record-table">
      <div class="record-row"><div class="record-cell">NAME</div></div>
      <div class="record-row"><div class="record-cell">DOB</div></div>
      <div class="record-row">
        <div class="record-cell record-cell--half">DATE</div>
        <div class="record-cell">TIME</div>
      </div>
      <div class="record-row"><div class="record-cell">TEMP °C</div></div>
      <div class="record-row"><div class="record-cell">SPECIMEN ID</div></div>
    </div>
    <div class="brand-strip">
      <div class="brand-mark">
        <span class="brand-dot"></span>
        <span class="brand-name">Vesk Lab Checks</span>
      </div>
      <div class="strip-rule" style="top:294px"></div>
      <div class="volume">90ml</div>
    </div>
  </section>

</body>
</html>
```